KVT Business Cards

We require business cards for our business. We would like a matte black back to the card, with our logo centred in the middle. The front side of the card is open to design.

Target Market(s)

Clients looking for legal services (professional)

Industry/Entity Type

Legal

Contact Information for Business Card

Boris Telemark
Partner
Mobile: 0438 715 642
Email: boris@kvtlaw.co
Website: www.kvtlaw.co
Level 3, 118 Wexbury Street
Sydney NSW 2000

Font styles to use
Other font styles liked:
• Avenir

Colors
f04a50
ffffff
1b1b1b

Requirements
Must have
• Black back with logo included in the centre of the card.
• Our font is Avenir.

```html
<!DOCTYPE html>
<html lang="en">
<head>
<meta charset="utf-8">
<title>KVT Business Cards</title>
<link rel="stylesheet" href="https://fonts.googleapis.com/css2?family=Nunito+Sans:wght@400;600;700;800&display=swap">
<style>
  :root {
    --ink: #070707;
    --paper: #ffffff;
    --crimson: #c0214a;
    --stage: #ececec;
    --text-dark: #1b1b1b;
  }
  * { margin: 0; padding: 0; box-sizing: border-box; }
  html, body {
    width: 1200px; height: 1200px; overflow: hidden;
    background: var(--stage);
    font-family: "Nunito Sans", "Avenir", sans-serif;
  }
  .sheet {
    width: 1200px; height: 1200px;
    display: flex; flex-direction: column;
    align-items: center; justify-content: center; gap: 64px;
  }
  .card {
    position: relative;
    width: 840px; height: 500px;
    box-shadow: 0 6px 22px rgba(0,0,0,0.12);
  }

  /* Back side */
  .card--back { background: var(--ink); }
  .brand {
    position: absolute; left: 185px; top: 150px;
    display: flex; align-items: center; gap: 48px;
  }
  .brand__mark {
    width: 96px; height: 96px;
    background: var(--crimson);
    transform: rotate(45deg);
  }
  .brand__name {
    color: var(--paper);
    font-weight: 700;
    font-size: 42px;
    line-height: 1.1;
    letter-spacing: 0.5px;
    white-space: nowrap;
  }
  .card--back .site {
    position: absolute; left: 0; right: 0; bottom: 68px;
    text-align: center;
    color: var(--crimson);
    font-size: 17px; letter-spacing: 0.5px;
  }

  /* Front side */
  .card--front { background: var(--paper); border: 1px solid #d6d6d6; }
  .holder {
    position: absolute; right: 472px; top: 212px;
    white-space: nowrap;
  }
  .holder__name {
    color: var(--crimson);
    font-weight: 800; font-size: 32px; line-height: 1;
    letter-spacing: -0.3px;
    text-transform: uppercase;
  }
  .holder__role {
    color: var(--text-dark);
    font-weight: 800; font-size: 20px; line-height: 1.2;
    text-transform: uppercase; margin-top: 4px;
  }
  .contact-rule {
    position: absolute; left: 386px; top: 112px;
    width: 3px; height: 278px; background: var(--crimson);
  }
  .contacts { position: absolute; left: 400px; top: 112px; list-style: none; }
  .contact {
    display: flex; align-items: center;
    height: 54px; margin-bottom: 21px;
  }
  .contact__icon { width: 52px; height: 54px; flex: none; }
  .contact__divider {
    width: 2px; height: 54px; background: var(--crimson);
    margin: 0 20px 0 10px;
  }
  .contact__text {
    color: var(--text-dark);
    font-size: 17px; line-height: 1.4;
    white-space: nowrap;
  }
</style>
</head>
<body>
<main class="sheet">

  <section class="card card--back" aria-label="Card back">
    <div class="brand">
      <div class="brand__mark" aria-hidden="true"></div>
      <div class="brand__name">KESSLER<br>VANE TELEMARK<br>LEGAL</div>
    </div>
    <p class="site">WWW.KVTLAW.CO</p>
  </section>

  <section class="card card--front" aria-label="Card front">
    <div class="holder">
      <p class="holder__name">Boris Telemark</p>
      <p class="holder__role">Designation</p>
    </div>
    <div class="contact-rule"></div>
    <ul class="contacts">
      <li class="contact">
        <svg class="contact__icon" viewBox="0 0 52 54" aria-hidden="true">
          <rect x="1" y="1" width="50" height="52" rx="10" fill="#070707"/>
          <path d="M1 30h50v13a10 10 0 0 1-10 10H11A10 10 0 0 1 1 43z" fill="#c0214a"/>
          <circle cx="26" cy="26" r="15" fill="none" stroke="#fff" stroke-width="3"/>
          <path d="M20 19c-2 2-1 7 3 11s9 5 11 3l-3-4-3 1c-2-1-4-3-5-5l1-3z" fill="#fff"/>
        </svg>
        <span class="contact__divider"></span>
        <span class="contact__text">0438 715 642</span>
      </li>
      <li class="contact">
        <svg class="contact__icon" viewBox="0 0 52 54" aria-hidden="true">
          <rect x="1" y="1" width="50" height="52" rx="10" fill="#070707"/>
          <path d="M1 30h50v13a10 10 0 0 1-10 10H11A10 10 0 0 1 1 43z" fill="#c0214a"/>
          <rect x="9" y="13" width="34" height="26" rx="3" fill="#fff"/>
          <path d="M14 35V19l12 10 12-10v16" fill="none" stroke="#070707" stroke-width="3.5" stroke-linejoin="round"/>
        </svg>
        <span class="contact__divider"></span>
        <span class="contact__text">boris@kvtlaw.co</span>
      </li>
      <li class="contact">
        <svg class="contact__icon" viewBox="0 0 52 54" aria-hidden="true">
          <rect x="1" y="1" width="50" height="52" rx="10" fill="#070707"/>
          <path d="M1 30h50v13a10 10 0 0 1-10 10H11A10 10 0 0 1 1 43z" fill="#c0214a"/>
          <g fill="none" stroke="#fff" stroke-width="2.5">
            <circle cx="26" cy="27" r="15"/>
            <ellipse cx="26" cy="27" rx="6.5" ry="15"/>
            <path d="M11 27h30M13 20h26M13 34h26"/>
          </g>
        </svg>
        <span class="contact__divider"></span>
        <span class="contact__text">www.kvtlaw.co</span>
      </li>
      <li class="contact">
        <svg class="contact__icon" viewBox="0 0 52 54" aria-hidden="true">
          <rect x="1" y="1" width="50" height="52" rx="10" fill="#070707"/>
          <path d="M1 24h50v19a10 10 0 0 1-10 10H11A10 10 0 0 1 1 43z" fill="#c0214a"/>
          <circle cx="26" cy="30" r="15" fill="#e2505f"/>
          <path d="M26 38c-5-6-7-9-7-12a7 7 0 0 1 14 0c0 3-2 6-7 12z" fill="#fff"/>
          <circle cx="26" cy="26" r="2.6" fill="#c0214a"/>
        </svg>
        <span class="contact__divider"></span>
        <span class="contact__text">Level 3, 118 Wexbury Street<br>Sydney NSW 2000</span>
      </li>
    </ul>
  </section>

</main>
</body>
</html>
```